Cutting edge Software Development Company needs to revamp it's website to reflect its growth ...

We would like to have our company website redone to have a more executive clean feel while still maintaining some level of playfulness. We currently offer bespoke Software's for Microfinance organizations on phone/mobile and Internet. Our development services could extend to selling you a platform outright or offering the platform as a service on either mobile or internet. Our corporate colors are Blue and White and we would like to see this reflected in the overall design. The final design should reflect a company thats making strides by helping our customers ideas come to life" a listening and caring partner!Current website: https://voltrix.co.ke/

Target Market(s)

Microfinance institutions that have a good customer base but do not have a back end or front end to support customers acquisition and servicing

Industry/Entity Type

Software Development

Number of Pages Required

5+ page

Font styles to use
Sans Serif

Colors
0255a3
0792cd
ffffff
cedeed
eaf1f7

Requirements
Must have
• Creative design
• Clean design
• Easy to navigate from page to page
Nice to have
• Blogs and Testimonials
Should not have
• Anything that would promote religious bias or show that we are not open to doing business with everyone.

```html
<!DOCTYPE html>
<html lang="en">
<head>
<meta charset="utf-8">
<title>Voltrix Technologies</title>
<link href="https://fonts.googleapis.com/css2?family=Open+Sans:wght@400;600;700;800&display=swap" rel="stylesheet">
<style>
:root{
  --blue:#0255a3;
  --sky:#0792cd;
  --white:#ffffff;
  --mist:#cedeed;
  --pale:#eaf1f7;
  --ink:#333c48;
  --muted:#6b7785;
}
*{box-sizing:border-box;margin:0;padding:0}
html,body{width:1200px;height:3504px;overflow:hidden}
body{font-family:"Open Sans",Arial,sans-serif;color:var(--ink);background:var(--white);font-size:14px;line-height:1.5}
.wrap{width:1000px;margin:0 auto;position:relative}
.section-title{font-size:30px;font-weight:700;color:var(--blue);text-align:center;text-transform:uppercase;letter-spacing:.5px}
.section-title::after{content:"";display:block;width:60px;height:3px;background:var(--sky);margin:10px auto 0}

/* header */
.topbar{height:112px;display:flex;align-items:center}
.topbar .wrap{display:flex;justify-content:space-between;align-items:center}
.brand{display:flex;align-items:center;gap:10px;font-size:30px;font-weight:800;color:var(--blue)}
.brand .dot{width:30px;height:30px;border-radius:50%;background:var(--sky)}
.contacts{display:flex;gap:26px;font-size:14px;color:var(--muted)}
.contacts span{display:flex;align-items:center;gap:6px}
.contacts svg{width:14px;height:14px;fill:var(--sky)}
.mainnav{height:40px;background:var(--blue)}
.mainnav ul{list-style:none;display:flex;justify-content:center;height:40px}
.mainnav li{color:var(--white);font-size:12px;font-weight:600;padding:0 22px;line-height:40px;text-transform:uppercase}
.mainnav li.active{background:var(--sky)}

/* hero */
.hero{height:508px;position:relative;background:linear-gradient(120deg,#c9d3dc 0%,#8e9aa6 35%,#55606b 70%,#38424c 100%);text-align:center;color:var(--white)}
.hero::before{content:"";position:absolute;inset:0;background:rgba(10,30,55,.25)}
.hero-text{position:relative;padding-top:180px}
.hero h1{font-size:44px;font-weight:800;text-transform:uppercase;line-height:1.1;letter-spacing:.5px}
.hero p{font-size:24px;margin-top:8px}
.dots{position:absolute;bottom:34px;left:0;right:0;display:flex;justify-content:center;gap:10px}
.dots i{width:26px;height:4px;background:rgba(255,255,255,.5)}
.dots i.on{background:var(--white)}

/* about */
.about{height:280px;padding-top:40px;text-align:center}
.about p{width:900px;margin:24px auto 0;font-size:13px;color:var(--muted);line-height:1.7}
.btn{display:inline-block;background:var(--blue);color:var(--white);font-size:13px;font-weight:600;padding:10px 26px;margin-top:22px;text-transform:uppercase}

/* services */
.services{height:520px;background:var(--pale);padding-top:46px}
.service-grid{display:grid;grid-template-columns:repeat(3,1fr);gap:46px 50px;margin-top:48px}
.service{display:flex;gap:16px}
.service .ico{flex:0 0 52px;height:52px;border-radius:50%;background:var(--white);border:2px solid var(--mist);display:flex;align-items:center;justify-content:center}
.service .ico svg{width:26px;height:26px;fill:none;stroke:var(--blue);stroke-width:2}
.service h3{font-size:15px;font-weight:700;color:var(--blue);text-transform:uppercase;line-height:1.25}
.service p{font-size:12px;color:var(--muted);margin-top:6px;line-height:1.55}

/* goals */
.goals{height:420px;padding-top:48px}
.goal-row{display:grid;grid-template-columns:repeat(4,1fr);gap:40px;margin-top:44px;text-align:center}
.goal .circle{width:96px;height:96px;border-radius:50%;background:var(--blue);margin:0 auto;display:flex;align-items:center;justify-content:center;box-shadow:0 0 0 6px var(--mist)}
.goal .circle svg{width:42px;height:42px;fill:none;stroke:var(--white);stroke-width:2.4;stroke-linecap:round;stroke-linejoin:round}
.goal h3{font-size:17px;font-weight:700;color:var(--sky);margin-top:26px;text-transform:uppercase}
.goal p{font-size:12px;color:var(--muted);margin-top:6px;line-height:1.55}

/* clients */
.clients{height:400px;background:var(--pale);padding-top:44px}
.client-row{display:grid;grid-template-columns:repeat(4,1fr);gap:24px;margin-top:42px}
.client{background:var(--white);padding:14px;box-shadow:0 2px 8px rgba(2,85,163,.1)}
.client .mark{height:96px;display:flex;align-items:center;justify-content:center;gap:8px;font-size:22px;font-weight:700}
.client .mark i{width:18px;height:18px;display:block}
.client p{font-size:12px;color:var(--muted);margin-top:10px;line-height:1.5}
.arrow{position:absolute;top:110px;font-size:34px;color:var(--ink);font-weight:300}
.arrow.l{left:-60px}.arrow.r{right:-60px}

/* testimonial */
.testimonial{height:380px;padding-top:70px;background:linear-gradient(#f5f8fb,#fff)}
.testimonial .wrap{display:flex;align-items:center}
.say{width:300px;background:var(--white);padding:36px 30px;box-shadow:0 2px 10px rgba(0,0,0,.08);position:relative;z-index:1}
.say h2{font-size:26px;font-weight:700;color:var(--blue);line-height:1.2;text-transform:uppercase}
.say .nav{margin-top:20px;font-size:26px;color:var(--muted);letter-spacing:14px}
.quote{flex:1;background:var(--white);padding:40px 60px 40px 70px;margin-left:-10px;box-shadow:0 2px 14px rgba(0,0,0,.1);position:relative;height:240px}
.quote .q{font-size:60px;font-weight:800;color:var(--blue);position:absolute;line-height:1}
.quote .q.open{left:20px;top:10px}.quote .q.close{right:24px;bottom:-10px}
.quote p{font-size:13px;color:var(--muted);line-height:1.7}
.quote .name{margin-top:16px;font-size:13px;color:var(--ink)}
.quote .co{font-size:12px;color:var(--muted)}

/* news */
.news{height:460px;padding-top:30px}
.news h2{font-size:30px;font-weight:700;color:var(--blue);text-transform:uppercase}
.news h2::after{content:"";display:block;width:60px;height:3px;background:var(--sky);margin-top:8px}
.news-row{display:grid;grid-template-columns:repeat(3,1fr);gap:26px;margin-top:34px}
.news .pic{height:180px}
.news h3{font-size:22px;font-weight:700;color:var(--blue);margin-top:14px}
.news p{font-size:12px;color:var(--muted);line-height:1.5;margin-top:4px}
.news a{font-size:12px;font-weight:700;color:var(--blue);text-decoration:none}

/* footer */
.footer{height:320px;background:var(--pale);padding-top:44px}
.footer .wrap{display:grid;grid-template-columns:150px 210px 150px 230px 1fr;gap:10px}
.footer h4{font-size:13px;font-weight:700;color:var(--blue);text-transform:uppercase;margin-bottom:12px}
.footer ul{list-style:none;font-size:12px;color:var(--muted);line-height:1.8}
.footer .cols{display:flex;gap:30px}
.footer .contact li{display:flex;gap:8px;align-items:flex-start}
.footer .contact svg{width:12px;height:12px;fill:var(--sky);margin-top:5px;flex:0 0 12px}
.subscribe input{width:100%;height:36px;border:1px solid var(--mist);padding:0 10px;font-family:inherit;font-size:12px;background:var(--white)}
.subscribe .btn{margin-top:10px;padding:8px 20px;font-size:12px}
.bottombar{height:64px;background:var(--blue);color:var(--white)}
.bottombar .wrap{display:flex;justify-content:space-between;align-items:center;height:64px;font-size:12px}
.socials{display:flex;gap:14px}
.socials i{width:18px;height:18px;border-radius:50%;background:var(--white);display:block;opacity:.9}
</style>
</head>
<body>

<header class="topbar">
  <div class="wrap">
    <div class="brand"><span class="dot"></span>Voltrix</div>
    <div class="contacts">
      <span><svg viewBox="0 0 24 24"><path d="M6.6 10.8a15.1 15.1 0 0 0 6.6 6.6l2.2-2.2a1 1 0 0 1 1-.25 11.4 11.4 0 0 0 3.6.57 1 1 0 0 1 1 1V20a1 1 0 0 1-1 1A17 17 0 0 1 3 4a1 1 0 0 1 1-1h3.5a1 1 0 0 1 1 1c0 1.25.2 2.45.57 3.57a1 1 0 0 1-.25 1z"/></svg>+254 700 418 320</span>
      <span><svg viewBox="0 0 24 24"><path d="M2 5h20v14H2zm2 2v.5l8 5 8-5V7z"/></svg>info@voltrix.co.ke</span>
    </div>
  </div>
</header>
<nav class="mainnav">
  <ul><li>Home</li><li>Services</li><li>Partners</li><li class="active">Our Goals</li><li>About Us</li><li>Demo</li><li>Prices</li><li>Contact</li><li>Policies</li></ul>
</nav>

<section class="hero" role="img" aria-label="Photo of a person working on a laptop with digital network graphics">
  <div class="hero-text">
    <h1>Welcome to the world of<br>innovation</h1>
    <p>Voltrix Technologies helps you to add value to your everyday ideas.</p>
  </div>
  <div class="dots"><i></i><i class="on"></i><i></i></div>
</section>

<section class="about">
  <h2 class="section-title">About our company</h2>
  <p>Voltrix Technologies LTD is a specialized IT company focused on end to end solutions for the financial sector. It is a privately owned company, designed to offer both professional consultancy services and development and delivery of software and infrastructure products that enable Sacco institutions to expand their outreach through the use of suitable technologies.</p>
  <span class="btn">Read More</span>
</section>

<section class="services">
  <div class="wrap">
    <h2 class="section-title">Our Services</h2>
    <div class="service-grid">
      <div class="service"><div class="ico"><svg viewBox="0 0 24 24"><rect x="3" y="4" width="18" height="13" rx="1"/><path d="M8 21h8M12 17v4"/></svg></div><div><h3>Web Application<br>Development</h3><p>Voltrix portal provide a range of features to enable finance institution serve its customer better and in efficient way.</p></div></div>
      <div class="service"><div class="ico"><svg viewBox="0 0 24 24"><rect x="7" y="2" width="10" height="20" rx="2"/><path d="M11 18h2"/></svg></div><div><h3>Mobile<br>Application</h3><p>Voltrix portal provide a range of features to enable finance institution serve its customer better and in efficient way.</p></div></div>
      <div class="service"><div class="ico"><svg viewBox="0 0 24 24"><circle cx="12" cy="12" r="3"/><path d="M12 2v3M12 19v3M2 12h3M19 12h3M4.9 4.9l2.1 2.1M17 17l2.1 2.1M4.9 19.1 7 17M17 7l2.1-2.1"/></svg></div><div><h3>Mobile Money<br>Integrations</h3><p>Voltrix portal provide a range of features to enable finance institution serve its customer better and in efficient way.</p></div></div>
      <div class="service"><div class="ico"><svg viewBox="0 0 24 24"><path d="M7 18h11a4 4 0 0 0 0-8 6 6 0 0 0-11.5 1.5A3.3 3.3 0 0 0 7 18z"/></svg></div><div><h3>Cloud<br>Services</h3><p>Voltrix portal provide a range of features to enable finance institution serve its customer better and in efficient way.</p></div></div>
      <div class="service"><div class="ico"><svg viewBox="0 0 24 24"><path d="M20 11a8 8 0 0 0-14.5-4.5M4 13a8 8 0 0 0 14.5 4.5M5 3v4h4M19 21v-4h-4"/></svg></div><div><h3>Custom<br>Solutions</h3><p>Voltrix portal provide a range of features to enable finance institution serve its customer better and in efficient way.</p></div></div>
      <div class="service"><div class="ico"><svg viewBox="0 0 24 24"><rect x="3" y="5" width="18" height="14" rx="1"/><path d="m3 6 9 7 9-7"/></svg></div><div><h3>SMS<br>Solution</h3><p>Voltrix portal provide a range of features to enable finance institution serve its customer better and in efficient way.</p></div></div>
    </div>
  </div>
</section>

<section class="goals">
  <div class="wrap">
    <h2 class="section-title">Our Goals</h2>
    <div class="goal-row">
      <div class="goal"><div class="circle"><svg viewBox="0 0 24 24"><path d="m8 7-5 5 5 5M16 7l5 5-5 5M14 4l-4 16"/></svg></div><h3>We Code</h3><p>We have cutting edge projects have been designed and managed by the company's development team members.</p></div>
      <div class="goal"><div class="circle"><svg viewBox="0 0 24 24"><path d="M9 18h6M10 21h4M12 3a6 6 0 0 0-3.5 10.9c.6.5 1 1.2 1 2.1h5c0-.9.4-1.6 1-2.1A6 6 0 0 0 12 3z"/></svg></div><h3>We Create</h3><p>The team of project managers in Voltrix Technologies has successfully implemented numerous international works.</p></div>
      <div class="goal"><div class="circle"><svg viewBox="0 0 24 24"><circle cx="12" cy="12" r="9"/><circle cx="12" cy="12" r="5"/><circle cx="12" cy="12" r="1"/></svg></div><h3>We Care</h3><p>Voltrix Technologies provides support for all its software products as a part of Service Level Agreements.</p></div>
      <div class="goal"><div class="circle"><svg viewBox="0 0 24 24"><path d="M14 4c3-1 6-1 6-1s0 3-1 6l-7 7-5-5zM7 11l-3 1 2 2M13 17l-1 3-2-2M9 15l-4 4"/></svg></div><h3>We Deliver</h3><p>Voltrix Technologies has a team of dedicated and experienced people who are available for both general support and specific.</p></div>
    </div>
  </div>
</section>

<section class="clients">
  <div class="wrap">
    <h2 class="section-title">Our Goals</h2>
    <span class="arrow l">&#8249;</span><span class="arrow r">&#8250;</span>
    <div class="client-row">
      <div class="client"><div class="mark" style="color:var(--blue)"><i style="background:var(--blue)"></i>Riverstone</div><p>Voltrix Core Banking<br>Riverstone Mobile Lending<br>Application</p></div>
      <div class="client"><div class="mark" style="color:#c0272d"><i style="background:#c0272d"></i>Pamoja</div><p>Voltrix Core Banking<br>Pamoja Mobile Lending<br>Application</p></div>
      <div class="client"><div class="mark" style="color:#222"><i style="background:#c0272d;border-radius:50%"></i>Tumaini Credit</div><p>Voltrix Core Banking<br>Tumaini Credit Mobile Lending<br>Application</p></div>
      <div class="client"><div class="mark" style="color:#1d2a36"><i style="background:#e8a020"></i>Kilele Sacco</div><p>Voltrix Core Banking<br>Kilele Mobile Lending<br>Application (USSD)</p></div>
    </div>
  </div>
</section>

<section class="testimonial">
  <div class="wrap">
    <div class="say"><h2>What our<br>customer says</h2><div class="nav">&#8249;&#8250;</div></div>
    <div class="quote">
      <span class="q open">&#8220;</span>
      <p>Our members now apply for loans from their phones and get answers in minutes. The team listened to what we needed, stayed with us through rollout and still answers every call quickly. Reporting is clearer and our staff spend far less time on manual work, so we can focus on serving more people every single day.</p>
      <div class="name">- Name Heading</div>
      <div class="co">Company Name</div>
      <span class="q close">&#8221;</span>
    </div>
  </div>
</section>

<section class="news">
  <div class="wrap">
    <h2>Latest News</h2>
    <div class="news-row">
      <article><div class="pic" role="img" aria-label="Photo of hands on a laptop with business icons" style="background:linear-gradient(135deg,#5a6b7d,#a8b6c4)"></div><h3>Nunc a ante id orci gravida</h3><p>Lorem ipsum dolor sit amet, consectetur adipiscing elit. Donec vitae mauris at purus tempus luctus sed non risus</p><a>Read More</a></article>
      <article><div class="pic" role="img" aria-label="Photo of a globe network with people icons" style="background:linear-gradient(135deg,#1f3c5e,#5c86b0)"></div><h3>Nunc a ante id orci gravida</h3><p>Lorem ipsum dolor sit amet, consectetur adipiscing elit. Donec vitae mauris at purus tempus luctus sed non risus</p><a>Read More</a></article>
      <article><div class="pic" role="img" aria-label="Photo of a desk with laptops and a phone" style="background:linear-gradient(135deg,#7f8c99,#d3dbe3)"></div><h3>Nunc a ante id orci gravida</h3><p>Lorem ipsum dolor sit amet, consectetur adipiscing elit. Donec vitae mauris at purus tempus luctus sed non risus</p><a>Read More</a></article>
    </div>
  </div>
</section>

<footer class="footer">
  <div class="wrap">
    <div class="cols">
      <div><h4>Site Map</h4><ul><li>Home</li><li>Services</li><li>Partners</li><li>Our Goals</li><li>About Us</li><li>Demo</li></ul></div>
      <div><h4>&nbsp;</h4><ul><li>Prices</li><li>Contact</li><li>Policies</li></ul></div>
    </div>
    <div><h4>What we offer</h4><ul><li>Core Banking Solutions</li><li>Mobile Applications</li><li>Cloud Solutions</li><li>Mobile Money Integrations</li><li>Bulk SMS</li><li>We Code</li></ul></div>
    <div><h4>&nbsp;</h4><ul><li>We Create</li><li>We Care</li><li>We Deliver</li><li>24/7 Support</li></ul></div>
    <div><h4>Contact Info</h4><ul class="contact">
      <li><svg viewBox="0 0 24 24"><path d="M12 2a7 7 0 0 0-7 7c0 5 7 13 7 13s7-8 7-13a7 7 0 0 0-7-7zm0 9.5A2.5 2.5 0 1 1 12 6.5a2.5 2.5 0 0 1 0 5z"/></svg>Upper Hill Plaza,<br>4th Floor Rd</li>
      <li><svg viewBox="0 0 24 24"><path d="M6.6 10.8a15.1 15.1 0 0 0 6.6 6.6l2.2-2.2a1 1 0 0 1 1-.25 11.4 11.4 0 0 0 3.6.57 1 1 0 0 1 1 1V20a1 1 0 0 1-1 1A17 17 0 0 1 3 4a1 1 0 0 1 1-1h3.5a1 1 0 0 1 1 1c0 1.25.2 2.45.57 3.57a1 1 0 0 1-.25 1z"/></svg>+254 700 418 320</li>
      <li><svg viewBox="0 0 24 24"><path d="M2 5h20v14H2zm2 2v.5l8 5 8-5V7z"/></svg>info@voltrix.co.ke</li>
      <li><svg viewBox="0 0 24 24"><path d="M12 2a10 10 0 1 0 0 20 10 10 0 0 0 0-20zm1 10V6h-2v7h6v-2z"/></svg>Daily: 9:00 am - 6:00 pm<br>Sunday: Closed</li>
    </ul></div>
    <div class="subscribe"><h4>Email Sign Up</h4><input type="text" value="Enter Email Address" aria-label="Email address"><span class="btn">Sign Up</span></div>
  </div>
</footer>
<div class="bottombar">
  <div class="wrap">
    <span>Copyright &copy; 2024 Voltrix Technologies. All Rights Reserved</span>
    <div class="socials"><i></i><i></i><i></i><i></i><i></i></div>
  </div>
</div>

</body>
</html>
```